Business Cards for IT Consulting Company (Managed Service Provider)

I am looking to have some business cards printed and would like some designs. We are an IT Consulting company based in Vancouver BC. I would like a nice clean and modern look to the cards. I have uploaded all the versions of my logo so parts can be used as needed. Here is a snippit from our website homepage:

Kelbrin Systems Ltd. is an IT Solutions Partner located in Vancouver BC, Canada. We offer IT solutions and support to customers in the greater Vancouver Area. With expertise in Quillara platforms, as well as Tovex and Bryn ZPL and over 12 years experience in the IT industry, Kelbrin Systems is dedicated to offering our clients top quality service and products. We take pride in the solutions we offer our customers. The greatest compliment a client can give us is to recommend our services.

Kelbrin Systems Ltd. offers a wide range of IT services from onsite service to remote support and managed service solutions. This allows clients to choose the support path that best suits their company’s needs. Supporting many different sized companies from small to enterprise level over the past 12 years Kelbrin Systems has the experience and expertise needed to ensure things run smoothly. Allowing our clients to focus on doing business.

Revolutionizing the way IT services are delivered.

Kelbrin Systems is dedicated to providing our clients with IT solutions that work and grow with them for years to come. This philosophy helps save money in the long run instead of replacing equipment constantly. Far too often IT solutions are not well thought out and while possibly solving the problem at hand, require replacement due to growth or quality within a very short time frame. Kelbrin Systems takes pride in providing solutions that will last and be able to accommodate growth without the need for replacement.

Industry/Entity Type

Information Technology

Contact Information for Business Card

Kelbrin Systems Ltd.
(Employee Name)
Eml: (Employees Email Address)
Web: kelbrinsys.me
Ph: 604-555-0142

Font styles to use
Serif
Sans Serif

Requirements
Must have
• The Company logo and company colors.
Nice to have
• - Our tag line: "Revolutionizing IT Services" or "Revolutionizing the way IT services are delivered."
• - Also I really like the idea of nature and technology together blending which is sort of where my logo came from so integrating that somehow onto the business cards would be great.

```html
<!DOCTYPE html>
<html lang="en">
<head>
<meta charset="utf-8">
<title>Kelbrin Systems – Business Cards</title>
<link href="https://fonts.googleapis.com/css2?family=Montserrat:wght@400;500;600;700&display=swap" rel="stylesheet">
<style>
  :root{
    --page:#dcdde0;
    --blue:#0aa0dd;
    --sky:#00aeef;
    --grey:#5f6064;
    --ink:#000;
    --white:#fff;
    --faint:#e6f3fb;
  }
  *{margin:0;padding:0;box-sizing:border-box}
  html,body{width:775px;height:1200px;overflow:hidden;background:var(--page);font-family:"Montserrat",Arial,sans-serif}
  .sheet{position:relative;width:775px;height:1200px}
  .card{position:absolute;width:285px;height:174px;background:var(--white);overflow:hidden}
  .card.rounded{border-radius:10px}
  .col-a{left:82px}.col-b{left:408px}
  .row-1{top:82px}.row-2{top:297px}.row-3{top:513px}.row-4{top:728px}.row-5{top:943px}
  .card--blue{background:var(--sky)}
  .card--black{background:var(--ink)}

  .brand{position:absolute;display:flex;align-items:center;gap:7px;color:var(--blue)}
  .brand-dot{width:30px;height:30px;border-radius:50%;border:2px solid currentColor;flex:none}
  .brand-name{font-weight:500;line-height:1}
  .brand-name b{display:block;font-weight:500;font-size:30px;letter-spacing:.3px}
  .brand-name span{display:block;font-size:10.5px;letter-spacing:.6px;margin-top:2px}
  .brand--white{color:var(--white)}
  .brand--sm .brand-dot{width:20px;height:20px}
  .brand--sm .brand-name b{font-size:19px}
  .brand--sm .brand-name span{font-size:6.5px}

  .decor{position:absolute}
  .decor--bold{background:linear-gradient(90deg,#0aa0dd 0%,#57c1ec 70%,#ffffff 100%)}
  .decor--faint{background:linear-gradient(90deg,#ffffff 0%,var(--faint) 40%,var(--faint) 100%)}

  .person{position:absolute}
  .person-name{font-size:10px;font-weight:700;color:var(--blue);letter-spacing:.3px}
  .person-role{font-size:7.2px;color:var(--grey);margin-top:1px}
  .person--grey .person-name{color:var(--grey)}
  .upper .person-role{text-transform:uppercase;letter-spacing:.3px;font-size:6.6px}

  .contacts{position:absolute;list-style:none;font-size:7.2px;color:var(--grey);line-height:10.4px}
  .contacts li{display:flex;align-items:center;gap:4px}
  .contacts svg{width:6px;height:6px;fill:var(--blue);flex:none}
  .contacts--right li{justify-content:flex-end}
  .contacts--light{color:var(--white)}

  .web-rule{position:absolute;left:0;right:0;bottom:19px;display:flex;align-items:center;justify-content:center;gap:5px;font-size:7.8px;font-weight:600;letter-spacing:.6px;color:var(--white)}
  .web-rule i{display:block;width:55px;height:1px}
  .web-rule i:first-child{background:linear-gradient(90deg,transparent,var(--white))}
  .web-rule i:last-child{background:linear-gradient(90deg,var(--white),transparent)}
</style>
</head>
<body>
<svg width="0" height="0" style="position:absolute" aria-hidden="true">
  <defs>
    <symbol id="ic-mail" viewBox="0 0 10 10"><path d="M0 2h10v6H0z M1 3l4 3 4-3" /></symbol>
    <symbol id="ic-phone" viewBox="0 0 10 10"><path d="M2 0l2 2.5-1.2 1.2a6 6 0 0 0 3.5 3.5L7.5 6 10 8l-1.5 2A9 9 0 0 1 0 1.5z"/></symbol>
    <symbol id="ic-web" viewBox="0 0 10 10"><circle cx="5" cy="5" r="5"/></symbol>
  </defs>
</svg>

<main class="sheet">

  <!-- Card: front with large mark area -->
  <section class="card col-a row-1">
    <div class="decor decor--bold" style="left:0;top:0;width:140px;height:174px" role="img" aria-label="Large blue hexagon brand decoration"></div>
    <div class="brand" style="left:133px;top:70px">
      <div class="brand-name"><b>kelbrin</b><span>SYSTEMS LTD.</span></div>
    </div>
  </section>

  <!-- Card: back with slanted footer -->
  <section class="card col-b row-1">
    <div class="brand" style="left:72px;top:18px">
      <span class="brand-dot"></span>
      <div class="brand-name"><b>kelbrin</b><span>SYSTEMS LTD.</span></div>
    </div>
    <div class="person" style="left:16px;top:108px">
      <div class="person-name">DORIAN VELL</div>
      <div class="person-role">Network Engineer</div>
    </div>
    <div style="position:absolute;left:16px;right:16px;top:133px;height:1px;background:#cfd0d2"></div>
    <ul class="contacts" style="left:16px;top:138px">
      <li><svg><use href="#ic-mail"/></svg>dvell@kelbrinsys.me</li>
      <li><svg><use href="#ic-phone"/></svg>604-555-0142</li>
    </ul>
    <svg style="position:absolute;left:0;top:142px" width="285" height="32" aria-hidden="true">
      <polygon points="0,26 158,26 156,32 0,32" fill="var(--sky)"/>
      <polygon points="168,0 285,0 285,32 158,32" fill="var(--grey)"/>
    </svg>
    <div style="position:absolute;right:16px;top:157px;font-size:8.4px;font-weight:700;color:var(--white)">www.kelbrinsys.me</div>
  </section>

  <!-- Card: blue front -->
  <section class="card rounded card--blue col-a row-2">
    <div class="brand brand--white" style="left:45px;top:66px">
      <span class="brand-dot"></span>
      <div class="brand-name"><b>kelbrin</b><span>SYSTEMS LTD.</span></div>
    </div>
    <div class="web-rule"><i></i>www.kelbrinsys.me<i></i></div>
  </section>

  <!-- Card: faint decoration back -->
  <section class="card rounded col-b row-2">
    <div class="decor decor--faint" style="left:115px;top:16px;width:170px;height:158px" role="img" aria-label="Faint hexagon brand decoration"></div>
    <div class="brand" style="left:16px;top:17px">
      <span class="brand-dot"></span>
      <div class="brand-name"><b>kelbrin</b><span>SYSTEMS LTD.</span></div>
    </div>
    <div style="position:absolute;left:0;top:100px;width:5px;height:25px;background:var(--sky)"></div>
    <div class="person person--grey" style="left:16px;top:104px">
      <div class="person-name">DORIAN VELL</div>
      <div class="person-role">Network Engineer</div>
    </div>
    <ul class="contacts" style="left:16px;top:129px">
      <li><svg><use href="#ic-mail"/></svg>dvell@kelbrinsys.me</li>
      <li><svg><use href="#ic-phone"/></svg>604-555-0142</li>
      <li><svg><use href="#ic-web"/></svg>www.kelbrinsys.me</li>
    </ul>
  </section>

  <!-- Card: black front -->
  <section class="card rounded card--black col-a row-3">
    <div class="brand" style="left:45px;top:66px">
      <span class="brand-dot"></span>
      <div class="brand-name"><b>kelbrin</b><span>SYSTEMS LTD.</span></div>
    </div>
    <div class="web-rule"><i></i>www.kelbrinsys.me<i></i></div>
  </section>

  <!-- Card: split white / black back -->
  <section class="card rounded col-b row-3">
    <div class="brand" style="left:45px;top:30px">
      <span class="brand-dot"></span>
      <div class="brand-name"><b>kelbrin</b><span>SYSTEMS LTD.</span></div>
    </div>
    <div style="position:absolute;left:0;right:0;top:99px;height:3px;background:var(--sky)"></div>
    <div style="position:absolute;left:0;right:0;top:102px;bottom:0;background:var(--ink)"></div>
    <div class="person upper" style="right:152px;top:128px;text-align:right">
      <div class="person-name">DORIAN VELL</div>
      <div class="person-role" style="color:var(--white)">Network Engineer</div>
    </div>
    <div style="position:absolute;left:143px;top:113px;width:1px;height:50px;background:#444"></div>
    <ul class="contacts contacts--light" style="left:153px;top:123px">
      <li><svg><use href="#ic-mail"/></svg>dvell@kelbrinsys.me</li>
      <li><svg><use href="#ic-phone"/></svg>604-555-0142</li>
      <li><svg><use href="#ic-web"/></svg>www.kelbrinsys.me</li>
    </ul>
  </section>

  <!-- Card: back with large mark area -->
  <section class="card col-b row-4">
    <div class="decor decor--bold" style="left:0;top:0;width:141px;height:174px" role="img" aria-label="Large blue hexagon brand decoration"></div>
    <div class="person upper" style="left:141px;top:61px">
      <div class="person-name">DORIAN VELL</div>
      <div class="person-role">Network Engineer</div>
    </div>
    <ul class="contacts" style="left:141px;top:86px">
      <li><svg><use href="#ic-mail"/></svg>dvell@kelbrinsys.me</li>
      <li><svg><use href="#ic-phone"/></svg>604-555-0142</li>
      <li><svg><use href="#ic-web"/></svg>www.kelbrinsys.me</li>
    </ul>
  </section>

  <!-- Card: single-side with divider -->
  <section class="card col-a row-5">
    <div class="brand brand--sm" style="left:15px;top:67px">
      <span class="brand-dot"></span>
      <div class="brand-name"><b>kelbrin</b><span>SYSTEMS LTD.</span></div>
    </div>
    <div style="position:absolute;left:143px;top:38px;width:1px;height:83px;background:#9a9b9e"></div>
    <div class="person person--grey upper" style="left:154px;top:57px">
      <div class="person-name">DORIAN VELL</div>
      <div class="person-role">Network Engineer</div>
    </div>
    <ul class="contacts" style="left:154px;top:81px">
      <li><svg><use href="#ic-mail"/></svg>dvell@kelbrinsys.me</li>
      <li><svg><use href="#ic-phone"/></svg>604-555-0142</li>
      <li><svg><use href="#ic-web"/></svg>www.kelbrinsys.me</li>
    </ul>
    <div style="position:absolute;left:0;right:0;top:154px;height:3px;background:var(--grey)"></div>
    <div style="position:absolute;left:0;right:0;top:158px;bottom:0;background:var(--sky)"></div>
  </section>

  <!-- Card: minimal back -->
  <section class="card col-b row-5">
    <div class="brand" style="left:16px;top:17px;gap:5px">
      <span class="brand-dot"></span>
      <div class="person" style="position:static">
        <div class="person-name">DORIAN VELL</div>
        <div class="person-role">Network Engineer</div>
      </div>
    </div>
    <ul class="contacts contacts--right" style="right:16px;top:127px">
      <li>dvell@kelbrinsys.me<svg><use href="#ic-mail"/></svg></li>
      <li>604-555-0142<svg><use href="#ic-phone"/></svg></li>
      <li>www.kelbrinsys.me<svg><use href="#ic-web"/></svg></li>
    </ul>
    <svg style="position:absolute;left:0;top:164px" width="285" height="10" aria-hidden="true">
      <polygon points="0,0 141,0 131,10 0,10" fill="var(--sky)"/>
      <polygon points="144,0 285,0 285,10 134,10" fill="var(--grey)"/>
    </svg>
  </section>

</main>
</body>
</html>
```